Design a label for Lunar Drift e liquid company

need a logo and five different fonts for each flavor
1. hats off tonight_ confetti cream cake
2. Red Velvet- red velvet Cake
3, Tiramisu- lady fingers soaked in expresso
4. Scone Crown- apple cinnamon muffin
5. Plum fold- blueberry turn over
these labels are going to be two different bottle sizes
30 ml and 60 ml with 3 different nicotine strengths
Target Market(s)
vapors that want dessert flavors
Industry/Entity Type
It Company
Contact Information for Business Card
will supply logo
Font styles to use
Other font styles liked:
- custom
Colors
Designer to choose colors to be used in the design.
Requirements
Must have
- custom logo and fonts
Nice to have
- ai files for multi color foil label printing

```html
<!DOCTYPE html>
<html lang="en">
<head>
<meta charset="utf-8">
<title>Lunar Drift – Hats Off Tonight Label</title>
<link rel="stylesheet" href="https://fonts.googleapis.com/css2?family=Arimo:wght@700&family=Lobster&family=Short+Stack&display=swap">
<style>
  :root {
    --stage: #d4d4d4;
    --teal: #17b3d2;
    --panel-light: #ffffff;
    --panel-soft: #eef8fc;
    --panel-mist: #bfe6f2;
    --title-blue: #2a82bd;
    --ink-dark: #3a3a3a;
    --ink-black: #111111;
    --sundae-cream: #f6e6b0;
    --sundae-choc: #7a4a2e;
    --sundae-pink: #f2a9b8;
    --bowl-grey: #a9b0b5;
  }
  * { margin: 0; padding: 0; box-sizing: border-box; }
  html, body {
    width: 1200px;
    height: 840px;
    overflow: hidden;
    background: var(--stage);
  }
  .canvas {
    position: relative;
    width: 1200px;
    height: 840px;
  }
  .label {
    position: absolute;
    left: 334px;
    top: 0;
    width: 531px;
    height: 840px;
    overflow: hidden;
    background: var(--teal);
  }
  .label-panel {
    position: absolute;
    inset: 0;
  }
  .brand {
    position: absolute;
    top: 36px;
    left: 0;
    width: 100%;
    display: flex;
    flex-direction: column;
    align-items: center;
    gap: 18px;
  }
  .brand-dot {
    width: 64px;
    height: 64px;
    border-radius: 50%;
    background: var(--ink-black);
  }
  .brand-name {
    font-family: "Arimo", sans-serif;
    font-weight: 700;
    font-size: 62px;
    line-height: 1;
    color: var(--ink-black);
    text-transform: uppercase;
    white-space: nowrap;
  }
  .flavor-art {
    position: absolute;
    left: 105px;
    top: 306px;
    width: 330px;
    height: 290px;
  }
  .flavor-name {
    position: absolute;
    top: 612px;
    left: 0;
    width: 100%;
    text-align: center;
    font-family: "Lobster", cursive;
    font-weight: 400;
    font-size: 66px;
    letter-spacing: 1px;
    color: var(--title-blue);
    line-height: 1;
    white-space: nowrap;
  }
  .flavor-desc {
    position: absolute;
    top: 694px;
    left: 0;
    width: 100%;
    text-align: center;
    font-family: "Short Stack", cursive;
    font-size: 36px;
    color: var(--ink-dark);
    line-height: 1;
    white-space: nowrap;
  }
  .volume {
    position: absolute;
    top: 796px;
    left: 0;
    width: 100%;
    text-align: center;
    font-family: "Arimo", sans-serif;
    font-weight: 700;
    font-size: 22px;
    line-height: 1;
    color: var(--ink-black);
  }
</style>
</head>
<body>
  <main class="canvas">
    <section class="label">
      <svg class="label-panel" width="531" height="840" viewBox="0 0 531 840" aria-hidden="true">
        <defs>
          <radialGradient id="panelGlow" cx="0.45" cy="0.45" r="0.75">
            <stop offset="0" stop-color="var(--panel-light)"/>
            <stop offset="0.6" stop-color="var(--panel-soft)"/>
            <stop offset="1" stop-color="var(--panel-mist)"/>
          </radialGradient>
        </defs>
        <polygon points="0,296 42,296 96,246 436,246 489,296 531,296 531,840 0,840" fill="url(#panelGlow)"/>
      </svg>

      <div class="brand">
        <span class="brand-dot" aria-hidden="true"></span>
        <span class="brand-name">Lunar Drift</span>
      </div>

      <svg class="flavor-art" viewBox="0 0 330 290" role="img" aria-label="Illustration of a banana split sundae with pink, chocolate and vanilla scoops, whipped cream and a cherry in a silver footed dish">
        <defs>
          <radialGradient id="sundaeTone" cx="0.5" cy="0.42" r="0.55">
            <stop offset="0" stop-color="var(--sundae-choc)" stop-opacity="0.75"/>
            <stop offset="0.35" stop-color="var(--sundae-pink)" stop-opacity="0.7"/>
            <stop offset="0.65" stop-color="var(--sundae-cream)" stop-opacity="0.65"/>
            <stop offset="0.85" stop-color="var(--bowl-grey)" stop-opacity="0.35"/>
            <stop offset="1" stop-color="var(--bowl-grey)" stop-opacity="0"/>
          </radialGradient>
        </defs>
        <ellipse cx="165" cy="145" rx="165" ry="145" fill="url(#sundaeTone)"/>
      </svg>

      <h1 class="flavor-name">Hats Off Tonight</h1>
      <p class="flavor-desc">Confetti Cream Cake</p>
      <p class="volume">30ml</p>
    </section>
  </main>
</body>
</html>
```